New design for a hotel booking website

I am looking to re-design my hotel booking website peakstaylodging.net. Please find the specs attached. Delivery in PSD format. Two pages total: (i) homepage and (ii) inner page.
I want the design to be very simple to navigate and have a feel that is related to Banff, Canada. You can keep a similar layout as the current website.
Requirements
1) Homepage
- Booking form above the fold containing the check in & check out dates, # of rooms and the Search button
- Quality image relating to the city of Banff to make it clear what city this is (no slider - I don't want any animation)
- A section for featured hotels (3-5 items)
- A section for links to other sections on the website (currently under "Explore Banff")
- A section for articles and local guides
- A weather widget (either in the header or somewhere else, similar to this one http://clipvanta.com/t/QX7RLPd2K4)
2) Hotel listings page - http://www.peakstaylodging.net/hotels
- Left or right sidebar – must contain the booking form with the same fields as on the homepage
- A section of why to book hotels with us under the booking form
- Each hotel listing should contain the following
Hotel name
Star rating
Short description (same as currently on the website)
Thumbnail
Address
A button to Check Rates
Notes
- I want the design to be user friendly, simple and easy to use
- I want it to be related to Banff. Banff is a resort town in Alberta, Canada with mountains for skiing in the winter and parks and wildlife nature in the summer.
- Delivery format: PSD
- I want the layout to be easily convertible into a responsive design
- Small social media icon to the Chatterly page (with the option to add Vidzo and Quippr in the future)
Some competing website examples:
1) corvelridgeway.com/Places-to-Stay/Hotels-Inns
2) tornivastays.org
Some examples of websites I liked:
1) http://www.quellmont.com/accommodation/hotels/
2) http://www.lodgevanterra.com/
Target Market(s)
Anyone looking to book their stay in Banff, AB, Canada.
Industry/Entity Type
Travel
Number of Pages Required
2 page
Look and feel

```html
<!DOCTYPE html>
<html lang="en">
<head>
<meta charset="utf-8">
<title>PeakStay Lodging – Compare prices on accommodations in Banff</title>
<link rel="stylesheet" href="https://fonts.googleapis.com/css2?family=Fira+Sans:wght@500;600&family=Roboto:wght@300;400;500;700&display=swap">
<style>
:root{
  --blue:#2a9fe0;
  --blue-dark:#1e8fd0;
  --sky:#a9d8f3;
  --ink:#2b2b2b;
  --grey:#8a8a8a;
  --nav:#4a4a4a;
  --panel:#2c2c2e;
  --orange:#f28a1a;
  --star:#f5a623;
  --line:#e2e2e2;
  --white:#ffffff;
}
*{box-sizing:border-box;margin:0;padding:0}
html,body{width:1071px;height:1200px;overflow:hidden}
body{position:relative;font-family:"Roboto",sans-serif;color:var(--ink);
  background:linear-gradient(180deg,var(--sky) 0%,#d6ecf9 45%,#f4f9fd 85%,#ffffff 100%)}
.abs{position:absolute}
.brand{left:98px;top:18px}
.brand-name{font-family:"Fira Sans",sans-serif;font-weight:600;font-size:25px;letter-spacing:-.3px;color:var(--blue-dark);line-height:26px}
.brand-tag{font-size:8px;color:var(--blue-dark);letter-spacing:.3px;margin-top:2px}
.promo{left:421px;top:29px;font-size:11.5px;color:var(--blue)}
.promo b{font-weight:500}
.social-dot{width:33px;height:33px;border-radius:50%;background:var(--blue)}
.weather{left:830px;top:29px;font-size:11.5px;font-weight:500;color:#4b4b4b}
.weather-icon{left:908px;top:19px;width:33px;height:33px;border-radius:50%;border:2px solid var(--blue);display:flex;align-items:center;justify-content:center}
.temp{left:947px;top:24px;font-size:18px;color:#4b4b4b}
.sheet{left:97px;top:70px;width:878px;height:1074px;background:var(--white);box-shadow:0 0 14px rgba(80,140,190,.12)}
.nav{left:122px;top:70px;height:42px;display:flex;align-items:center;font-size:11.5px;color:var(--nav);letter-spacing:.3px}
.nav a{color:inherit;text-decoration:none;position:relative}
.nav a.active{color:var(--blue)}
.nav a.active::before{content:"";position:absolute;left:0;top:-14px;width:31px;height:3px;background:var(--blue)}
.nav .sep{color:#b0b0b0;margin:0 29px}
.hero{left:122px;top:113px;width:827px;height:333px;background:linear-gradient(160deg,#6aaee6 0%,#cfe4f3 35%,#8a5a3c 55%,#e6eef5 75%,#b8cde0 100%)}
.badge-title{left:165px;top:335px;background:var(--blue);color:#fff;font-weight:700;font-size:20px;padding:3px 8px}
.badge-sub{left:165px;top:370px;background:var(--panel);color:#fff;font-size:12px;padding:4px 8px}
.search{left:674px;top:132px;width:259px;height:295px;background:var(--panel);padding:12px 26px 0 26px;color:#fff}
.search h2{font-family:"Fira Sans",sans-serif;font-weight:500;font-size:16px;letter-spacing:.3px}
.search p{color:var(--blue);font-size:11px;line-height:14px;margin-top:4px;padding-bottom:8px;border-bottom:2px solid var(--blue)}
.field-label{font-size:11px;margin-top:9px;margin-bottom:4px}
.input{height:29px;background:#fff;color:#bdbdbd;font-size:10.5px;display:flex;align-items:center;justify-content:space-between;padding:0 7px}
.select{width:100px}
.btn{display:inline-block;margin-top:12px;width:100px;height:29px;background:var(--blue);color:#fff;font-family:"Fira Sans",sans-serif;font-weight:500;font-size:15px;text-align:center;line-height:29px}
.rule{height:3px;background:var(--blue)}
.section-title{font-family:"Fira Sans",sans-serif;font-weight:500;font-size:15px;letter-spacing:.3px;color:#2e2e2e}
.card{top:507px;width:160px;height:194px;border:1px solid var(--line);background:#fff}
.card.raised{box-shadow:0 2px 6px rgba(0,0,0,.22)}
.card-photo{height:122px}
.card-body{padding:9px 8px 0}
.card-name{font-size:12px;color:#2d2d2d}
.card-price{font-size:11px;color:var(--orange);margin-top:3px}
.stars{margin-top:5px;display:flex;gap:1px}
.about{left:122px;top:760px;width:215px;font-size:11.5px;line-height:19.6px;color:var(--grey);font-weight:300}
.tile{background:#ccc}
.caption{font-size:11.5px;color:#333}
.explore{left:741px;top:780px;list-style:none;font-size:11.5px;color:#7c7c7c}
.explore li{height:22.6px;display:flex;align-items:center;gap:10px}
.explore li.on{color:var(--blue)}
.footer{left:97px;top:1032px;width:878px;height:111px;background:var(--blue);color:#fff}
.foot-links{font-size:10px;display:flex;gap:23px}
.copy{font-size:9.5px}
.ring{width:26px;height:26px;border-radius:50%;border:2px solid #fff}
.foot-brand{font-family:"Fira Sans",sans-serif;font-weight:600;font-size:16px;line-height:17px;text-align:right}
.foot-tag{font-size:6px;text-align:right;letter-spacing:.2px}
</style>
</head>
<body>

<header>
  <div class="abs brand">
    <div class="brand-name">PEAKSTAYLODGING</div>
    <div class="brand-tag">COMPARE PRICES ON ACCOMMODATIONS IN BANFF</div>
  </div>
  <div class="abs promo"><b>Like us on Chatterly</b> for a chance to win a free 2-night stay in Banff!</div>
  <div class="abs social-dot" style="left:781px;top:19px" aria-label="Chatterly"></div>
  <div class="abs weather">Mostly Cloudy</div>
  <div class="abs weather-icon">
    <svg width="20" height="14" viewBox="0 0 20 14"><path d="M5 13h10a4 4 0 0 0 0-8 5 5 0 0 0-9.5 1A3.5 3.5 0 0 0 5 13z" fill="none" stroke="#2a9fe0" stroke-width="1.6"/></svg>
  </div>
  <div class="abs temp">0<sup style="font-size:10px">o</sup>C</div>
</header>

<div class="abs sheet"></div>

<nav class="abs nav">
  <a class="active" href="#">HOME</a><span class="sep">/</span>
  <a href="#">BANFF HOTELS</a><span class="sep">/</span>
  <a href="#">BANFF RESORTS</a><span class="sep">/</span>
  <a href="#">LODGES</a><span class="sep">/</span>
  <a href="#">INNS &amp; MOTELS</a>
</nav>

<main>
  <div class="abs hero" role="img" aria-label="Snow-covered timber lodge among pine trees and mountains in Banff"></div>
  <div class="abs badge-title">Best Selection</div>
  <div class="abs badge-sub">Choose from over 47 hotels, resorts and inns in Banff</div>

  <form class="abs search">
    <h2>SEARCH BANFF HOTELS</h2>
    <p>Enter your travel dates and find available accommodations.</p>
    <div class="field-label">Check-in</div>
    <div class="input">mm/dd/yyyy<svg width="11" height="12"><rect x=".5" y="1.5" width="10" height="10" fill="none" stroke="#ccc"/><path d="M1 4h9M3 6h1M6 6h1M3 8h1M6 8h1" stroke="#ccc"/></svg></div>
    <div class="field-label">Check-out</div>
    <div class="input">mm/dd/yyyy<svg width="11" height="12"><rect x=".5" y="1.5" width="10" height="10" fill="none" stroke="#ccc"/><path d="M1 4h9M3 6h1M6 6h1M3 8h1M6 8h1" stroke="#ccc"/></svg></div>
    <div class="field-label">Rooms</div>
    <div class="input select">1 Room<svg width="8" height="5"><path d="M0 0h8L4 5z" fill="#888"/></svg></div>
    <div class="btn">SEARCH</div>
  </form>

  <section>
    <div class="abs rule" style="left:122px;top:462px;width:129px"></div>
    <h2 class="abs section-title" style="left:122px;top:478px">FEATURED HOTELS</h2>

    <article class="abs card raised" style="left:122px">
      <div class="card-photo" role="img" aria-label="Castle-style hotel lit up at dusk" style="background:linear-gradient(180deg,#1b4fa8,#0f2c66)"></div>
      <div class="card-body"><div class="card-name">Aldercrest Springs Resort</div><div class="card-price">from $445 CAD</div>
      <div class="stars"><svg width="60" height="10" viewBox="0 0 60 10"><g fill="#f5a623"><path id="s" d="M5 0l1.5 3.3 3.5.3-2.7 2.3.9 3.5L5 7.5 1.8 9.4l.9-3.5L0 3.6l3.5-.3z"/><use href="#s" x="12"/><use href="#s" x="24"/><use href="#s" x="36"/><use href="#s" x="48"/></g></svg></div></div>
    </article>
    <article class="abs card" style="left:289px">
      <div class="card-photo" role="img" aria-label="Indoor hot pool with stone pillars" style="background:linear-gradient(180deg,#b9a58c,#5e4a3a)"></div>
      <div class="card-body"><div class="card-name">Stonegate Resort Hotel</div><div class="card-price">from $445 CAD</div>
      <div class="stars"><svg width="60" height="10" viewBox="0 0 60 10"><g fill="#f5a623"><use href="#s"/><use href="#s" x="12"/><use href="#s" x="24"/><use href="#s" x="36"/><use href="#s" x="48"/></g></svg></div></div>
    </article>
    <article class="abs card" style="left:456px">
      <div class="card-photo" role="img" aria-label="Wooden lodge surrounded by summer garden" style="background:linear-gradient(180deg,#5c8a3a,#a06a3a 60%,#4d7a2e)"></div>
      <div class="card-body"><div class="card-name">Elkhorn Ridge Lodge</div><div class="card-price">from $445 CAD</div>
      <div class="stars"><svg width="60" height="10" viewBox="0 0 60 10"><g fill="#f5a623"><use href="#s"/><use href="#s" x="12"/><use href="#s" x="24"/><use href="#s" x="36"/><use href="#s" x="48"/></g></svg></div></div>
    </article>
    <article class="abs card" style="left:622px">
      <div class="card-photo" role="img" aria-label="Hotel room with bed and fireplace" style="background:linear-gradient(180deg,#e8e1d4,#7a4a32)"></div>
      <div class="card-body"><div class="card-name">Northpine Royal Canadian</div><div class="card-price">from $445 CAD</div>
      <div class="stars"><svg width="60" height="10" viewBox="0 0 60 10"><g fill="#f5a623"><use href="#s"/><use href="#s" x="12"/><use href="#s" x="24"/><use href="#s" x="36"/><use href="#s" x="48"/></g></svg></div></div>
    </article>
    <article class="abs card" style="left:789px">
      <div class="card-photo" role="img" aria-label="Snowy hotel rooftops with mountains" style="background:linear-gradient(180deg,#3c7fc4,#e8eef3 45%,#9a4a22)"></div>
      <div class="card-body"><div class="card-name">Marten Hotel and Suites</div><div class="card-price">from $445 CAD</div>
      <div class="stars"><svg width="60" height="10" viewBox="0 0 60 10"><g fill="#f5a623"><use href="#s"/><use href="#s" x="12"/><use href="#s" x="24"/><use href="#s" x="36"/><use href="#s" x="48"/></g></svg></div></div>
    </article>
  </section>

  <section>
    <div class="abs rule" style="left:122px;top:737px;width:206px"></div>
    <h2 class="abs section-title" style="left:122px;top:751px">ACCOMMODATIONS IN BANFF</h2>
    <p class="abs about" style="top:777px">Banff, conveniently located in the Alberta's Rockies, is the largest city in the Banff National Park. Banff is one of the most popular tourist destinations in Canada. It is well known for its hot springs and mountainous surroundings. Tourists may enjoy a variety of activities such as hiking, biking, skiing and more.</p>

    <div class="abs tile" style="left:362px;top:737px;width:177px;height:106px;background:linear-gradient(180deg,#f2f0ee,#b8202a)" role="img" aria-label="Champagne and roses"></div>
    <div class="abs caption" style="left:362px;top:847px">Romantic Banff getaway hotels</div>
    <div class="abs tile" style="left:362px;top:866px;width:177px;height:106px;background:linear-gradient(180deg,#6b6b6b,#8c5a34)" role="img" aria-label="Two dogs beside a suitcase"></div>
    <div class="abs caption" style="left:362px;top:977px">Banff pet friendly hotels</div>
    <div class="abs tile" style="left:546px;top:737px;width:177px;height:235px;background:linear-gradient(180deg,#d9c6b4,#c9e4ee)" role="img" aria-label="Couple relaxing in a hot tub"></div>
    <div class="abs caption" style="left:546px;top:977px">Banff hotels with hot-tub</div>

    <div class="abs rule" style="left:741px;top:737px;width:206px"></div>
    <h2 class="abs section-title" style="left:741px;top:751px">EXPLORE BANFF</h2>
    <ul class="abs explore">
      <li class="on"><svg width="5" height="8"><path d="M.5.5 4 4 .5 7.5" fill="none" stroke="currentColor"/></svg>Things to do in Banff</li>
      <li><svg width="5" height="8"><path d="M.5.5 4 4 .5 7.5" fill="none" stroke="currentColor"/></svg>Banff Festivals</li>
      <li><svg width="5" height="8"><path d="M.5.5 4 4 .5 7.5" fill="none" stroke="currentColor"/></svg>Experience Summit Gondola</li>
      <li><svg width="5" height="8"><path d="M.5.5 4 4 .5 7.5" fill="none" stroke="currentColor"/></svg>Heli Sightseeing in Banff</li>
      <li><svg width="5" height="8"><path d="M.5.5 4 4 .5 7.5" fill="none" stroke="currentColor"/></svg>Hiking in Banff</li>
      <li><svg width="5" height="8"><path d="M.5.5 4 4 .5 7.5" fill="none" stroke="currentColor"/></svg>Camping &amp; Campgrounds</li>
      <li><svg width="5" height="8"><path d="M.5.5 4 4 .5 7.5" fill="none" stroke="currentColor"/></svg>Hotels near Upper Hot Springs</li>
      <li><svg width="5" height="8"><path d="M.5.5 4 4 .5 7.5" fill="none" stroke="currentColor"/></svg>Nearby Cities</li>
    </ul>
  </section>
</main>

<footer class="abs footer">
  <div class="abs foot-links" style="left:24px;top:26px"><span>HOME</span><span>BANFF HOTELS</span><span>BANFF RESORTS</span><span>LODGES</span><span>INNS &amp; MOTELS</span></div>
  <div class="abs foot-links" style="left:24px;top:49px"><span>CONTACTS</span><span>FAQ</span><span>TERMS &amp; CONDITIONS</span><span>PRIVACY POLICY</span></div>
  <div class="abs copy" style="left:24px;top:70px">Copyright © 2016 PeakStayLodging.net, All Rights Reserved.</div>
  <div class="abs copy" style="left:665px;top:23px;font-size:10px">Like us on Chatterly</div>
  <div class="abs ring" style="left:763px;top:16px" aria-label="Chatterly"></div>
  <div class="abs ring" style="left:794px;top:16px" aria-label="Quippr"></div>
  <div class="abs ring" style="left:825px;top:16px" aria-label="Vidzo"></div>
  <div class="abs" style="right:28px;top:56px">
    <div class="foot-brand">PEAKSTAYLODGING</div>
    <div class="foot-tag">COMPARE PRICES ON ACCOMMODATIONS IN BANFF</div>
  </div>
</footer>

</body>
</html>
```